Indian Takeaway Menu -

I would like to have double parallel fold A4 sheet menu.
A4 sheet cut in half and attached to the other half to make the sheet 4 small pages long.

Colors
abd036
ffffff

Requirements
Must have
• Please check new attachments - menu size and layout is not correct.
• I would like to add Dark brown colour. A4 sheet folded 4x Menu layout pocket size.
Nice to have
• Dark Brown - Parrot Green and very light Brown

```html
<!DOCTYPE html>
<html lang="en">
<head>
<meta charset="utf-8">
<title>Saffron Hearth – Takeaway Menu</title>
<link href="https://fonts.googleapis.com/css2?family=Oswald:wght@500&family=Open+Sans:ital,wght@0,400;0,600;0,700;1,400&family=Merriweather:wght@700;900&display=swap" rel="stylesheet">
<style>
:root{
  --brown:#5b3b2b;
  --green:#abd036;
  --green-deep:#8fb23a;
  --paper:#ffffff;
  --backdrop:#7a7a7a;
  --ink:#1e1e1e;
  --muted:#4a4a4a;
  --orange:#f0a22a;
  --red:#d3272c;
  --light-brown:#e9dccd;
}
*{margin:0;padding:0;box-sizing:border-box}
html,body{width:1200px;height:1200px;overflow:hidden;background:var(--backdrop)}
body{font-family:"Open Sans",Arial,sans-serif;color:var(--ink)}
.stage{position:absolute;left:0;top:0;width:1500px;height:1500px;transform:scale(.8);transform-origin:0 0}
.sheet{position:absolute;background:var(--paper);box-shadow:0 6px 14px rgba(0,0,0,.35)}
.sheet--outer{left:25px;top:199px;width:1450px;height:511px}
.sheet--inner{left:25px;top:832px;width:1455px;height:513px}
.abs{position:absolute}
.ribbon{position:absolute;height:30px;background:var(--brown);color:#fff;font-family:"Oswald",sans-serif;font-weight:500;font-size:20px;display:flex;align-items:center;justify-content:center;letter-spacing:-.2px;
  clip-path:polygon(0 0,100% 0,96% 50%,100% 100%,0 100%,4% 50%)}
.item{position:absolute}
.row{display:flex;align-items:baseline;font-size:11px;font-weight:600;white-space:nowrap}
.lead{flex:1;border-bottom:1px solid #8a8a8a;margin:0 5px;transform:translateY(-2px)}
.price{font-weight:600}
.desc{font-size:6.6px;line-height:1.4;color:var(--muted);margin-top:3px}
.desc-price{display:flex;align-items:flex-end;gap:8px}
.desc-price .price{font-size:11px}
.photo{position:absolute;border-radius:2px}
.photo--curry{background:radial-gradient(circle at 50% 55%,#e08a2c,#b95a1c 45%,#5e3a22 80%)}
.photo--spice{background:radial-gradient(circle at 55% 40%,#e34d2b,#f2b12d 40%,#8a5a34 65%,#fff 90%)}
.photo--plate{background:radial-gradient(circle at 50% 50%,#e9dccd,#c98a4a 55%,#8a5a34)}
/* meal deals */
.setmeals{position:absolute;left:65px;top:429px;width:289px;height:274px;background:linear-gradient(160deg,#c9c9c2,#9f9784 50%,#c08a4a);}
.setmeal{position:absolute;top:21px;height:250px;background:rgba(143,178,58,.88);color:#fff;padding:6px 6px}
.setmeal h4{font-weight:400;font-size:14px;text-align:center;line-height:1.4}
.setmeal ul{list-style:none;font-size:7.5px;line-height:2.4;margin-top:6px}
/* info */
.info{position:absolute;left:377px;top:588px;width:373px;height:122px;background:var(--green);color:#fff;padding:10px 0 0 25px}
.info .addr{font-size:15px;font-weight:700;line-height:1.4}
.info .mail{font-size:12.5px;font-weight:700;margin-top:16px}
.info .note{font-size:9.5px;margin-top:12px;padding-left:14px}
.hours{position:absolute;left:750px;top:199px;width:365px;height:102px;background:var(--brown);color:#fff;padding:18px 0 0 17px}
.hours .label{font-size:16px;position:absolute;left:17px;top:18px}
.hours .times{position:absolute;left:147px;top:22px;font-size:9.5px;line-height:1.35}
.hours .phone{position:absolute;left:147px;top:68px;font-size:15px}
.brand{position:absolute;left:764px;top:368px;display:flex;align-items:center;gap:6px;font-weight:700;font-size:19px;color:var(--brown)}
.brand .dot{width:12px;height:12px;background:var(--orange);border-radius:50%}
.brand-tag{position:absolute;left:783px;top:396px;font-size:5px;letter-spacing:1.2px;color:var(--brown)}
.hero{position:absolute;left:762px;font-family:"Merriweather",Georgia,serif;line-height:1}
.hero--a{top:423px;font-size:34px;color:#4a4a4a}
.hero--b{top:470px;font-size:37px;color:var(--orange)}
.hero--c{top:512px;font-size:46px;color:var(--red);font-weight:900}
.hero--d{top:570px;font-size:22px;color:var(--green-deep)}
.hero--e{top:597px;font-size:15px;color:var(--brown)}
.web{position:absolute;left:818px;top:670px;font-size:12px;letter-spacing:5px;font-weight:600}
.band{position:absolute;left:750px;top:697px;width:365px;height:13px;background:var(--brown)}
.legend{position:absolute;left:1137px;top:604px;font-size:8.5px;line-height:1.65}
.healthy .row{font-size:13px;font-weight:400}
.healthy .lead{border:0}
.healthy .desc{font-size:7px}
/* nan */
.nan-head{position:absolute;left:1144px;top:898px;color:var(--brown);font-size:14px;line-height:1.3}
.nanlist{position:absolute;left:1144px;top:937px;width:292px;list-style:none}
.nanlist li{display:flex;align-items:baseline;height:24.4px;font-size:11.5px}
.nanlist li .lead{border-bottom:1px solid #aaa;margin:0 0 0 2px}
.nanlist li .price{font-size:10.5px;font-weight:700}
.low{position:absolute;left:53px;top:264px;color:var(--red);font-style:italic;font-size:11.5px}
.choose{position:absolute;left:52px;top:283px;font-size:12px;font-weight:600}
</style>
</head>
<body>
<div class="stage">

<!-- ================= OUTER SIDE ================= -->
<section class="sheet sheet--outer"></section>

<div class="ribbon" style="left:68px;top:228px;width:277px">Meal Deals only €8.50</div>
<p class="low">(Low Fat Dishes)</p>
<p class="choose">Choose with Rice or Plain Naan</p>
<div class="item" style="left:52px;top:304px;width:148px"><div class="row">Chicken Dupiaza<span class="lead"></span><span class="price">€8.50</span></div><p class="desc">Chicken cooked with ginger and chunks of onions and finished with onion seeds….</p></div>
<div class="item" style="left:219px;top:304px;width:150px"><div class="row">Chicken Rogan josh<span class="lead"></span><span class="price">€8.50</span></div><p class="desc">A red chicken curry prepared with fresh herb &amp; spices, a delicacy from Kashmir</p></div>
<div class="item" style="left:52px;top:363px;width:148px"><div class="row">Chicken Bhuna<span class="lead"></span><span class="price">€8.50</span></div><p class="desc">Tomatoes and onion sauce cooked with black peppers &amp; spring onions.</p></div>
<div class="item" style="left:219px;top:361px;width:150px"><div class="row">Tarkari Makhani<span class="lead"></span><span class="price">€8.50</span></div><p class="desc">Mixed seasonal vegetables in a smooth tikka masala sauce</p></div>

<div class="setmeals" role="img" aria-label="Photo of crispy onion bhajia on a plate">
  <div class="setmeal" style="left:12px;width:84px"><h4>Set Meal 1<br>€16</h4><ul><li>- Onion bhajia</li><li>- Chicken Tikka Masala</li><li>- Poppadoms</li><li>- Pilau rice</li><li>- Naan</li></ul></div>
  <div class="setmeal" style="left:100px;width:85px"><h4>Set Meal 2<br>€28.00</h4><ul><li>- Onion bhajia</li><li>- Chicken tikka</li><li>- Chicken Tikka Masala</li><li>- Lamb Roganjosh</li><li>- 2xPilau rice</li><li>- 1xNaan</li><li>- Poppadom</li></ul></div>
  <div class="setmeal" style="left:188px;width:87px"><h4>Set Meal 3/4<br>€45</h4><ul><li>- Onion bhajia</li><li>- Vegetable samosa</li><li>- Chicken tikka</li><li>- Chicken Tikka Masala</li><li>- Lamb Roganjosh</li><li>- Sambhar Veg Curry</li><li>- 2 x Pilau Rice</li><li>- 2 x Naan</li><li>- Poppadom</li></ul></div>
</div>

<div class="ribbon" style="left:418px;top:228px;width:277px">Vegetarian Dishes</div>
<div class="item" style="left:388px;top:268px;width:160px"><div class="row">Shahi Paneer 3, 5<span class="lead"></span><span class="price">€9.25</span></div><p class="desc">Indian cheese in semi-dry sauce.</p></div>
<div class="item" style="left:566px;top:267px;width:152px"><div class="row">Karahi Paneer 3<span class="lead"></span><span class="price">€9.25</span></div><p class="desc">Colorful curry is prepared using homemade Indian cheese (paneer)</p></div>
<div class="item" style="left:388px;top:308px;width:160px"><div class="row">Subz Maloni Mild<span class="lead"></span><span class="price">€9.25</span></div><p class="desc">Stir fried vegetables with ground spices.</p></div>
<div class="item" style="left:566px;top:311px;width:152px"><div class="row">Saag Paneer<span class="lead"></span><span class="price">€9.25</span></div><p class="desc">Pan fried cottage cheese &amp; spinach with kasoori methi &amp; fresh coriander</p></div>
<div class="item" style="left:388px;top:341px;width:160px"><div class="row">Dum Wale Aloo3<span class="lead"></span><span class="price">€9.25</span></div><p class="desc">Potatoes cooked with ginger, garlic,<br>onions, yoghurt &amp; curry leave with<br>cumin Flavored.</p></div>
<div class="item" style="left:566px;top:351px;width:152px"><div class="row">Vegetable Biryani<span class="lead"></span><span class="price">€9.25</span></div><p class="desc">Basmati Rice cooked with vegetables, fresh herbs, spices &amp; fried golden onion. Comes with curry sauce.</p></div>
<div class="item" style="left:388px;top:392px;width:160px"><div class="row">Sambhar Vegetable Curry 4yv</div><div class="desc desc-price"><span>Vegetable curry cooked with lentil, curry<br>leaves, and mustard seeds</span><span class="price" style="color:var(--ink);font-weight:600">€9.25</span></div></div>
<div class="photo photo--curry" style="left:444px;top:441px;width:238px;height:135px" role="img" aria-label="Photo of a paneer curry in a copper serving bowl"></div>

<div class="info">
  <p class="addr"><svg width="11" height="14" viewBox="0 0 11 14" style="vertical-align:-1px"><path d="M5.5 0A5.5 5.5 0 0 0 0 5.5C0 9.5 5.5 14 5.5 14S11 9.5 11 5.5A5.5 5.5 0 0 0 5.5 0zm0 7.8a2.3 2.3 0 1 1 0-4.6 2.3 2.3 0 0 1 0 4.6z" fill="#fff"/></svg> Unit 4, Birchmore Yard, Glenvale,<br>IR, A00 X000</p>
  <p class="mail"><svg width="11" height="8" viewBox="0 0 11 8"><rect width="11" height="8" fill="#fff"/><path d="M0 0l5.5 4.5L11 0" stroke="#abd036" fill="none"/></svg> orders@saffronhearth.example</p>
  <p class="note">All our meals are cooked to order.</p>
</div>

<div class="hours">
  <p class="label">Opening Hours:</p>
  <p class="times">Sun - Thurs 5PM to 10.00PM<br>Fri - Sat 5.00PM-10.30PM<br>Deliveries From 5.30PM</p>
  <p class="phone"><svg width="12" height="12" viewBox="0 0 24 24"><path d="M6.6 10.8a15 15 0 0 0 6.6 6.6l2.2-2.2c.3-.3.7-.4 1-.2 1.1.4 2.3.6 3.6.6.6 0 1 .4 1 1V20c0 .6-.4 1-1 1A17 17 0 0 1 3 4c0-.6.4-1 1-1h3.5c.6 0 1 .4 1 1 0 1.3.2 2.5.6 3.6.1.3 0 .7-.2 1z" fill="#fff"/></svg> 015550142 | 015550143</p>
</div>
<div class="brand"><span class="dot"></span>Saffron Hearth</div>
<p class="brand-tag">AUTHENTIC INDIAN FOOD AT HOME</p>
<p class="hero hero--a">Authentic</p>
<p class="hero hero--b">INDIAN</p>
<p class="hero hero--c">FOOD</p>
<p class="hero hero--d">DELIVERED</p>
<p class="hero hero--e">TO YOU AT HOME</p>
<div class="photo photo--spice" style="left:920px;top:320px;width:185px;height:340px;border-radius:40%" role="img" aria-label="Photo of stacked wooden bowls filled with red chilli, turmeric and green spice powders"></div>
<p class="web">www.saffronhearth.example</p>
<div class="band"></div>

<div class="ribbon" style="left:1160px;top:227px;width:277px">Healthy Side orders</div>
<div class="healthy">
<div class="item" style="left:1137px;top:266px;width:296px"><div class="row">Sautéed Broccoli<span class="lead"></span><span class="price">€5.00</span></div><p class="desc">Broccoli, green beans and spinach leaves<br>sautéed with roasted cumin and fresh garlic.</p></div>
<div class="item" style="left:1137px;top:309px;width:296px"><div class="row">Chana Saag<span class="lead"></span><span class="price">€5.50</span></div><p class="desc">Chickpeas cooked with chopped spinach,<br>onion, and cumin and finished with cream</p></div>
<div class="item" style="left:1137px;top:352px;width:296px"><div class="row">Chana Masala &nbsp;v<span class="lead"></span><span class="price">€5.50</span></div><p class="desc">Chickpeas simmered with tomato, caramelised<br>onion, black pepper and fresh coriander.</p></div>
<div class="item" style="left:1137px;top:396px;width:296px"><div class="row">Aloo Saag &nbsp;&nbsp;3 yv<span class="lead"></span><span class="price">€5.50</span></div><p class="desc">Crispy Potato with spinach, caramelised onion,<br>garam masala and a dash of cream.</p></div>
<div class="item" style="left:1135px;top:449px;width:298px"><div class="row">Aloo Ghobhi &nbsp;&nbsp;v<span class="lead"></span><span class="price">€5.50</span></div><p class="desc">Crispy Potatoes cubes &amp; Cauliflower cooked<br>with roasted cumin with tomato and onion</p></div>
<div class="item" style="left:1135px;top:499px;width:298px"><div class="row">Tarka Daal &nbsp;4 y v<span class="lead"></span><span class="price">€5.00</span></div><p class="desc">Home style soaked yellow chana cooked with<br>cumin &amp; garam masala.</p></div>
<div class="item" style="left:1135px;top:542px;width:298px"><div class="row">Tangy &nbsp;Aloo &nbsp;&nbsp;&nbsp;&nbsp;v<span class="lead"></span><span class="price">€5.00</span></div><p class="desc">Crispy Potatoes cubes cooked with roasted<br>cumin and touch of our tangy sauce</p></div>
</div>
<p class="legend">Y: can be cooked without allergen<br>H: Healthy Option<br>V: Suitable for Vegans</p>
<div class="photo photo--curry" style="left:1300px;top:588px;width:105px;height:105px;border-radius:50%" role="img" aria-label="Photo of chickpea curry in a copper handi"></div>

<!-- ================= INNER SIDE ================= -->
<section class="sheet sheet--inner"></section>

<div class="ribbon" style="left:95px;top:858px;width:240px">Starters</div>
<div class="item" style="left:50px;top:903px;width:157px"><div class="row">Onion Bhajia<span class="lead"></span><span class="price">€4.50</span></div><p class="desc">Spinach &amp; onions fritters flavored<br>with mild spices</p></div>
<div class="item" style="left:222px;top:903px;width:149px"><div class="row">Chicken Pakora<span class="lead"></span><span class="price">€5.50</span></div><p class="desc">Boneless pieces of chicken coated in<br>gram flour batter, with spices.</p></div>
<div class="item" style="left:50px;top:943px;width:157px"><div class="row">Vegetable Samosa 2<span class="lead"></span><span class="price">€4.50</span></div><p class="desc">Crispy Pastry stuffed with potatoes, chick peas, Green peas mixed with desi spices until golden.</p></div>
<div class="item" style="left:222px;top:949px;width:149px"><div class="row">Chicken Wings &nbsp;2,1<span class="lead"></span><span class="price">€5.50</span></div></div>
<div class="item" style="left:50px;top:991px;width:157px"><div class="row">Palak Tikki<span class="lead"></span><span class="price">€4.50</span></div><p class="desc">Cakes of fresh spinach and chana dal</p></div>
<div class="item" style="left:222px;top:976px;width:149px"><div class="row">Tandoori Mix Meat Platter 3</div><div class="desc desc-price"><span>Our special tandoori assortment of<br>tandoori chicken on bone, seekh<br>kebab and chicken tikka.</span><span class="price" style="color:var(--ink);font-weight:600;margin-bottom:10px">€9.50</span></div></div>
<div class="item" style="left:50px;top:1026px;width:157px"><div class="row">Veg Pakora<span class="lead"></span><span class="price">€5.00</span></div><p class="desc">Cauliflower, potato and broccoli,<br>golden fried with Gram flour batter</p></div>
<div class="item" style="left:222px;top:1026px;width:149px"><div class="row">Mix Veg platter 2<span class="lead"></span><span class="price">€7.00</span></div><p class="desc">Veg Samosa, Onion Bhaji, Veg<br>Pakora</p></div>
<div class="item" style="left:50px;top:1073px;width:157px"><div class="row">Keema Singhara 2<span class="lead"></span><span class="price">€5.00</span></div><p class="desc">Spicy seasoned mince lamb in light<br>pastry</p></div>
<div class="item" style="left:222px;top:1070px;width:149px"><div class="row">Chicken Tikka 3<span class="lead"></span><span class="price">€5.00</span></div><p class="desc">Tender chicken marinated overnight<br>with yoghurt, spices charred in<br>tandoor</p></div>

<div class="ribbon" style="left:95px;top:1124px;width:240px">Kebab- on Nan Bread</div>
<div class="item" style="left:50px;top:1169px;width:157px"><div class="row">Doner Kebab 2,3,6<span class="lead"></span><span class="price">€8.50</span></div><p class="desc">Stripes of minced chicken &amp; beef served<br>with garlic mayo, chilli sauce &amp; mixed<br>salad &amp; wrapped in naan.</p></div>
<div class="item" style="left:222px;top:1169px;width:153px"><div class="row">Seekh Kebab<span class="lead"></span><span class="price">€5.50</span></div><p class="desc">Skewered hand pounder lamb<br>glazed in tandoor with green<br>chilli &amp; black cardamom</p></div>
<div class="item" style="left:50px;top:1224px;width:157px"><div class="row">Chicken Tikka &nbsp;Kebab<span class="lead"></span><span class="price">€8.50</span></div><p class="desc">Chicken breast marinated in spices,<br>barbecued served with garlic<br>mayo, chilli sauce &amp; mixed salad &amp;<br>wrapped in naan</p></div>
<div class="item" style="left:224px;top:1226px;width:153px"><div class="row">Mix &nbsp;Kebab &nbsp;2,3,6<span class="lead"></span><span class="price">€8.50</span></div><p class="desc">Pieces of chicken tikka &amp; donner meat<br>with garlic mayo, sweet chilli &amp; salad<br>wrapped in naan bread</p></div>
<div class="item" style="left:48px;top:1288px;width:161px"><div class="row">Garlic Chips<span class="lead"></span><span class="price">€4.00</span></div></div>
<div class="item" style="left:48px;top:1309px;width:161px"><div class="row">Garlic Cheese Chips<span class="lead"></span><span class="price">€5.00</span></div></div>
<div class="photo photo--plate" style="left:228px;top:1278px;width:127px;height:57px" role="img" aria-label="Photo of chicken tikka kebab skewers"></div>

<div class="ribbon" style="left:437px;top:858px;width:243px">Chef Rana's Special Curries</div>
<div class="item" style="left:387px;top:902px;width:178px"><div class="row">Butter Murgh &nbsp;3,5<span class="lead"></span><span class="price">€11.00</span></div><p class="desc">Chicken cooked in tandoor mixed with rich<br>Tomato creamy cashew sauce, splash of<br>cream with hint of honey &amp; dry fenugreek.</p></div>
<div class="item" style="left:577px;top:902px;width:176px"><div class="row">Shahi Veg Kofta 3'5<span class="lead"></span><span class="price">€11.00</span></div><p class="desc">Handmade veg and panner dumplings simmered<br>in tomato sauce, musky fenugreek sauce finished<br>with touch of honey and cream.</p></div>
<div class="item" style="left:387px;top:949px;width:163px"><div class="row">Laal Maas<span class="lead"></span><span class="price">€12</span></div><p class="desc">Taditional rajasthani lamb cooked with garlic<br>and ginger , degi chilli powder, tomatoes<br>finished with star aniseed and clove powder.</p></div>
<div class="item" style="left:387px;top:998px;width:163px"><div class="row">Kerala Prawn14<span class="lead"></span><span class="price">€12</span></div><p class="desc">Delicacy of kerala spices, tomato and red<br>onion gravy finished with touch of fresh<br>coconut milk.</p></div>
<div class="photo photo--curry" style="left:580px;top:959px;width:138px;height:71px" role="img" aria-label="Photo of a curry bowl with rice and spices"></div>

<div class="ribbon" style="left:500px;top:1057px;width:180px">Chicken Dishes</div>
<div class="item" style="left:389px;top:1098px;width:176px"><div class="row">Punjabi Saag 3 y<span class="lead"></span><span class="price">€10.50</span></div><p class="desc">Chicken cooked with spinach, ginger, garlic,<br>fresh cream &amp; temperd with Punjabi tarka.</p></div>
<div class="item" style="left:573px;top:1097px;width:179px"><div class="row">Chicken Karahi<span class="lead"></span><span class="price">€9.25</span></div><p class="desc">Boneless chicken Prepared in Deg with<br>peppers,onion, tomatoes and Indian<br>whole spices.</p></div>
<div class="item" style="left:389px;top:1141px;width:172px"><div class="row">Royale Korma3, 5<span class="lead"></span><span class="price">€9.50</span></div><p class="desc">Breast of chicken cooked in a rich creamy<br>sauce with saffron &amp; coconut , probably<br>most popular among Irish.</p></div>
<div class="item" style="left:573px;top:1149px;width:179px"><div class="row">Chicken Tikka Masala 3<span class="lead"></span><span class="price">€9.25</span></div><p class="desc">Chicken roasted in clayoven and simmered<br>in smooth creamy tomato sauce with palm<br>crushed fenugreek leaves and jiggery .</p></div>
<div class="item" style="left:389px;top:1189px;width:172px"><div class="row">Chicken Dahiwala &nbsp;3<span class="lead"></span><span class="price">€9.25</span></div><p class="desc">Amazingly spicy chicken curry cooked with<br>yogurt, green chillies, ginger and herbs.</p></div>
<div class="item" style="left:573px;top:1202px;width:179px"><div class="row">South Indian Garlic Chilli<span class="lead"></span><span class="price">€9.25</span></div><p class="desc">Chicken cooked in south Indian style and<br>loaded with garlic, ground spices, fresh herbs</p></div>
<div class="item" style="left:389px;top:1230px;width:178px"><div class="row">Murgh Biryani &nbsp;3,5,y<span class="lead"></span><span class="price">€10.95</span></div><p class="desc">Perfumed basmati rice with chicken<br>cubes, nuts , golden onions and biryani<br>spices , served with sauce.</p></div>
<div class="item" style="left:389px;top:1285px;width:176px"><div class="row">Saffron Hearth Chicken Curry<span class="lead"></span><span class="price">€9.25</span></div><p class="desc">Traditional curry cooked with coconut<br>,mustard seed , cashews and curry leaves.</p></div>
<div class="photo photo--curry" style="left:587px;top:1247px;width:126px;height:85px" role="img" aria-label="Photo of chicken curry with rice"></div>

<div class="ribbon" style="left:820px;top:857px;width:240px">Lamb Dishes</div>
<div class="item" style="left:762px;top:899px;width:175px"><div class="row">Lamb Madras<span class="lead"></span><span class="price">€10.95</span></div><p class="desc">The popular dish of madras cooked with<br>plum tomato , degi chilli , coconut and<br>finished with hint of lemon juice.</p></div>
<div class="item" style="left:958px;top:898px;width:158px"><div class="row">Lamb Kohlapuri<span class="lead"></span><span class="price">€11.95</span></div><p class="desc">Cauliflower, potato and broccoli, golden<br>fried with Gram flour batter</p></div>
<div class="item" style="left:762px;top:952px;width:175px"><div class="row">Palak Gosht 3, y<span class="lead"></span><span class="price">€10.95</span></div><p class="desc">Pan-fried lamb pieces cooked with<br>spinach, fresh herbs, ginger and touch<br>of cream</p></div>
<div class="item" style="left:958px;top:943px;width:158px"><div class="row">Lamb Jalferzi<span class="lead"></span><span class="price">€11.95</span></div><p class="desc">Lamb, tossed with cubes of onions,<br>peppers flavored with crushed coriander<br>seeds and dry fenugreek with hint of<br>cream.</p></div>
<div class="item" style="left:762px;top:998px;width:175px"><div class="row">Lamb Roganjosh<span class="lead"></span><span class="price">€10.95</span></div><p class="desc">Slow cooked tender lamb in kashmiri style<br>with fresh herbs and Himalayan spices.</p></div>
<div class="item" style="left:958px;top:1002px;width:158px"><div class="row">Gosht Biryani 3,5,y<span class="lead"></span><span class="price">€11.95</span></div><p class="desc">Aged rice cooked with tender land brown<br>onions, home made masala and<br>accompanied with curry sauce.</p></div>
<div class="photo photo--plate" style="left:762px;top:1042px;width:170px;height:74px" role="img" aria-label="Photo of roast lamb shank with vegetables"></div>

<div class="ribbon" style="left:820px;top:1134px;width:240px">Prawn Dishes</div>
<div class="item" style="left:764px;top:1179px;width:171px"><div class="row">Prawn Masala &nbsp;3<span class="lead"></span><span class="price">€11.95</span></div><p class="desc">Prawns in a smooth creamy sauce<br>flavoured with kasoori methi &amp; tandoori<br>spices.</p></div>
<div class="item" style="left:959px;top:1179px;width:148px"><div class="row">Prawn Bhuna<span class="lead"></span><span class="price">€11.95</span></div><p class="desc">Prawns cooked in onions &amp; tomato<br>with black pepper to bought together<br>the kick of spices</p></div>
<div class="item" style="left:764px;top:1230px;width:171px"><div class="row">Prawn Karahi<span class="lead"></span><span class="price">€11.95</span></div><p class="desc">Prawns cooked with peppers, spring onion,<br>Caramelised onion ,tomatoes &amp; whole spices</p></div>
<div class="item" style="left:957px;top:1233px;width:151px"><div class="row">Prawn Biryani 3,6,y<span class="lead"></span><span class="price">€11.95</span></div></div>
<div class="item" style="left:764px;top:1276px;width:171px"><div class="row">Goan Prawn Curry3,4,5<span class="lead"></span><span class="price">€11.95</span></div><p class="desc">Fisherman`s favourite prawn curry aromatic with<br>coconut , mustard , nuts ,curryleaves and spices<br>fron goa's costal area.</p></div>
<div class="photo photo--curry" style="left:967px;top:1258px;width:112px;height:82px" role="img" aria-label="Photo of prawn curry in a white bowl"></div>

<div class="ribbon" style="left:1183px;top:860px;width:239px">Nan Bread</div>
<p class="nan-head">Side Orders<br>All naan bread contains 2,3,6</p>
<ul class="nanlist">
  <li>Naan.<span class="lead"></span><span class="price">€2.20</span></li>
  <li>Garlic Naan<span class="lead"></span><span class="price">€2.50</span></li>
  <li>Garlic Chilli Naan<span class="lead"></span><span class="price">€3.00</span></li>
  <li>Peshwari Naan..5<span class="lead"></span><span class="price">€3.00</span></li>
  <li>Keema Naan.<span class="lead"></span><span class="price">€3.20</span></li>
  <li>Coriander Naan.<span class="lead"></span><span class="price">€2.50</span></li>
  <li>Chilli Cheese Naan<span class="lead"></span><span class="price">€3.50</span></li>
  <li>G.O.C<span class="lead"></span><span class="price">€3.00</span></li>
  <li>Boiled Basmati<span class="lead"></span><span class="price">€2.00</span></li>
  <li>Pilau Rice<span class="lead"></span><span class="price">€2.00</span></li>
  <li>Lemon Rice<span class="lead"></span><span class="price">€3.00</span></li>
  <li>Poppodum(2)<span class="lead"></span><span class="price">€2.50</span></li>
  <li>Riata ….3<span class="lead"></span><span class="price">€2.50</span></li>
</ul>
<div class="photo photo--plate" style="left:1207px;top:1256px;width:170px;height:78px" role="img" aria-label="Photo of garlic naan bread on a board"></div>

</div>
</body>
</html>
```